Inspiration Poster

Inspirational Poster that has a Kamran Dulo like abstract look (http://www.vexalo.com/images/search?q=kamran+dulo&FORM=HDRSC2) with the text:

"we walk not in order to arrive at the promise land but because walking itself is a revolution"
-Peter Ambrick

```html
<!DOCTYPE html>
<html lang="en">
<head>
<meta charset="utf-8">
<title>Walking Is a Revolution — Poster</title>
<link rel="stylesheet" href="https://fonts.googleapis.com/css2?family=Sorts+Mill+Goudy:ital@0;1&display=swap">
<style>
  :root {
    --ink-light: #f6f1e4;
    --tone-violet: #3a3350;
    --tone-blue: #4d6f86;
    --tone-red: #c8452f;
    --tone-orange: #d98a3a;
    --tone-teal: #4f9c94;
    --tone-olive: #8f9a3e;
    --tone-moss: #5f7a2e;
    --tone-sand: #c9b75a;
    --tone-deep: #2c3a22;
  }
  html, body {
    margin: 0;
    padding: 0;
    width: 798px;
    height: 1200px;
    overflow: hidden;
    background: var(--tone-olive);
  }
  .poster {
    position: relative;
    width: 798px;
    height: 1200px;
    overflow: hidden;
    font-family: "Sorts Mill Goudy", "Georgia", serif;
    color: var(--ink-light);
  }
  .poster__artwork {
    position: absolute;
    inset: 0;
    background:
      radial-gradient(ellipse 260px 380px at 400px 180px, rgba(40, 34, 60, 0.85), transparent 70%),
      radial-gradient(ellipse 240px 300px at 90px 420px, rgba(200, 69, 47, 0.85), transparent 70%),
      radial-gradient(ellipse 180px 240px at 250px 420px, rgba(217, 138, 58, 0.7), transparent 70%),
      radial-gradient(ellipse 280px 420px at 720px 460px, rgba(79, 156, 148, 0.85), transparent 70%),
      radial-gradient(ellipse 300px 200px at 130px 120px, rgba(77, 111, 134, 0.8), transparent 70%),
      radial-gradient(ellipse 420px 300px at 300px 980px, rgba(201, 183, 90, 0.7), transparent 70%),
      radial-gradient(ellipse 300px 260px at 700px 1050px, rgba(44, 58, 34, 0.75), transparent 70%),
      linear-gradient(180deg, var(--tone-violet) 0%, var(--tone-blue) 25%, var(--tone-moss) 60%, var(--tone-olive) 80%, var(--tone-moss) 100%);
  }
  .poster__quote {
    position: absolute;
    left: 34px;
    top: 978px;
    margin: 0;
    font-style: italic;
    font-size: 29px;
    line-height: 46px;
    letter-spacing: 0.2px;
    text-shadow: 0 1px 3px rgba(0, 0, 0, 0.35);
  }
  .poster__quote span { display: block; white-space: nowrap; }
  .poster__author {
    position: absolute;
    right: 36px;
    top: 1120px;
    margin: 0;
    font-style: italic;
    font-size: 34px;
    text-shadow: 0 1px 3px rgba(0, 0, 0, 0.35);
  }
</style>
</head>
<body>
  <main class="poster">
    <div class="poster__artwork" role="img" aria-label="Abstract motion-blurred street scene with walking figures in streaks of red, teal, violet and olive light"></div>
    <blockquote class="poster__quote">
      <span>we walk</span>
      <span>not in order to arrive at the promise land</span>
      <span>but because walking itself is a revolution</span>
    </blockquote>
    <p class="poster__author">Peter Ambrick</p>
  </main>
</body>
</html>
```